Quarnel Asset Exchange (Trading Platform)

We need a design of Quarnel Asset Exchange Trading Platform.

Please find attached a mock up of VelmoraTrade design this has to be redesigned based on plinor.co.uk style.

Industry/Entity Type

Digital

```html
<!DOCTYPE html>
<html lang="en">
<head>
<meta charset="utf-8">
<title>Quarnel Asset Exchange – Trading</title>
<link href="https://fonts.googleapis.com/css2?family=Arimo:wght@400;700&display=swap" rel="stylesheet">
<style>
:root{
  --blue:#0e9bd5;--blue-bright:#08a8e6;--dark:#4a4a4a;--grey:#d3d3d3;--grey-light:#e4e4e4;
  --text:#333;--white:#fff;--buy:#bfe9d6;--buy-alt:#d4f3e6;--buy-text:#1a7a3c;
  --sell:#ebbbbd;--sell-alt:#f4d1d2;--sell-text:#b0121a;--line:#c8c8c8;
}
*{box-sizing:border-box;margin:0;padding:0}
html,body{width:1200px;height:1104px;overflow:hidden}
body{position:relative;background:var(--white);font-family:"Arimo",sans-serif;color:var(--text);font-size:12px}
.abs{position:absolute}
.brand{left:110px;top:56px;width:150px;font-size:16px;line-height:20px;font-weight:400;color:var(--dark)}
.brand-rule{left:271px;top:40px;width:1px;height:78px;background:var(--dark)}
.brand-dot{width:16px;height:16px;border-radius:50%;background:var(--blue)}
.nav{left:289px;top:93px;font-size:12px;color:#555}
.nav a{color:#555;text-decoration:none}.nav a.active{color:var(--blue)}
.field{height:23px;border:1px solid #bbb;border-radius:2px;padding:4px 7px;color:#777;font-size:12px}
.btn{height:23px;border-radius:3px;color:#fff;font-size:11px;padding:5px 8px;text-align:center}
.forgot{left:673px;top:95px;font-size:9px;color:#666}
.ticker{left:0;top:124px;width:1200px;height:48px;background:var(--blue);color:#fff}
.tick{position:absolute;top:8px}
.tick small{display:block;font-size:11px;margin-bottom:3px}
.tick b{font-weight:400;font-size:16px}
.tick-sep{position:absolute;top:0;width:1px;height:48px;background:rgba(255,255,255,.4)}
.coin{left:237px;top:10px;width:30px;height:30px;border-radius:50%;border:3px solid #fff}
.panel-head{height:24px;background:var(--blue);color:#fff;font-size:14px;padding:4px 11px}
.row{height:24px;padding:5px 11px;display:flex;font-size:12px}
.row:nth-child(odd){background:var(--grey)}.row:nth-child(even){background:var(--grey-light)}
.tabs{display:flex;height:22px;font-size:12px}
.tabs span{padding:4px 7px;background:var(--dark);color:#fff}
.tabs span.on{background:var(--blue)}
.chart-bar{left:290px;top:210px;width:540px;height:50px;background:var(--dark)}
.ctrl{position:absolute;top:10px;height:30px;background:var(--blue);color:#fff;font-weight:700;font-size:12px;text-align:center;padding-top:8px}
.caret{position:absolute;top:10px;width:22px;height:30px;background:var(--blue);border-left:1px solid rgba(255,255,255,.5)}
.caret:after{content:"";position:absolute;left:7px;top:13px;border:4px solid transparent;border-top:5px solid #fff}
.tool-bar{left:290px;top:260px;width:540px;height:53px;background:var(--grey)}
.dates span{position:absolute;top:590px;font-size:12px;color:#555}
.obook .row span:first-child{width:116px}
.b1{background:var(--buy)!important;color:var(--buy-text)}.b2{background:var(--buy-alt)!important;color:var(--buy-text)}
.s1{background:var(--sell)!important;color:var(--sell-text)}.s2{background:var(--sell-alt)!important;color:var(--sell-text)}
.footer{left:0;top:812px;width:1200px;height:292px;background:var(--blue);color:#fff}
.fcol{position:absolute;top:36px}
.fcol h3{font-size:22px;font-weight:700;margin-bottom:3px}
.fcol p{font-size:12px;line-height:18px}
.social{width:29px;height:29px;border-radius:50%;background:#fff;display:inline-block;margin-right:7px}
</style>
</head>
<body>
<div class="abs brand">Quarnel Asset Exchange</div>
<div class="abs brand-rule"></div>
<div class="abs brand-dot" style="left:285px;top:52px"></div>
<nav class="abs nav"><a class="active">Home</a> · <a>About Us</a> · <a>Trade</a> · <a>News</a> · <a>Fees</a> · <a>FAQ</a> · <a>Contact us</a></nav>
<div class="abs field" style="left:671px;top:67px;width:130px">Email</div>
<div class="abs field" style="left:806px;top:67px;width:130px">Password</div>
<div class="abs btn" style="left:944px;top:67px;width:66px;background:var(--dark)">Log In</div>
<div class="abs btn" style="left:1015px;top:67px;width:74px;background:var(--blue)">Sign Up</div>
<div class="abs forgot">Forgot your password?</div>

<div class="abs ticker">
  <div class="abs coin"></div>
  <div class="tick" style="left:281px"><small>Current Price</small><b>$444.13</b></div>
  <div class="tick-sep" style="left:372px"></div>
  <div class="tick" style="left:434px"><small>Daily Change</small><b>-9.54</b> <span style="font-size:10px">-2.10%</span></div>
  <div class="tick-sep" style="left:516px"></div>
  <div class="tick" style="left:552px"><small>Day's Range</small><b>$440.00 - $457.30</b></div>
  <div class="tick-sep" style="left:715px"></div>
  <div class="tick" style="left:751px"><small>Today's Open</small><b>$453.57</b></div>
  <div class="tick-sep" style="left:852px"></div>
  <div class="tick" style="left:888px"><small>24h Volume</small><b>7194 BTC</b></div>
</div>

<section class="abs" style="left:129px;top:210px;width:140px">
  <div class="panel-head" style="display:flex;justify-content:space-between"><span>PAIR</span><span>PRICE</span></div>
  <div>
    <div class="row"><span style="width:68px">BTC/USD</span><span style="color:#c22">↓</span>&nbsp;634.12</div>
    <div class="row"><span style="width:68px">LTC/USD</span><span style="color:#c22">↓</span>&nbsp;23.23</div>
    <div class="row"><span style="width:68px">LTC/BTC</span><span style="color:#2a8a2a">↑</span>&nbsp;0.0123</div>
  </div>
</section>
<section class="abs" style="left:129px;top:331px;width:140px">
  <div class="panel-head">YOUR BALANCE</div>
  <div>
    <div class="row"><span style="width:62px">BTC</span>0.92176</div>
    <div class="row"><span style="width:62px">LTC</span>0</div>
    <div class="row"><span style="width:62px">USD</span>1987.45</div>
  </div>
</section>
<section class="abs" style="left:129px;top:449px;width:140px;height:329px;background:var(--grey)">
  <div class="tabs"><span class="on" style="padding:4px 6px">Chat</span><span style="padding:4px 5px">News</span><span style="padding:4px 5px;flex:1">Chirpline</span></div>
  <div style="padding:17px 10px 10px;line-height:14px;font-size:12px">
    <p style="margin-bottom:5px"><span style="color:var(--blue)">User1:</span> Hello!</p>
    <p style="margin-bottom:5px"><span style="color:var(--blue)">User2:</span> Hi</p>
    <p><span style="color:var(--blue)">User1:</span> Long time no see. How have been?</p>
  </div>
  <div class="abs" style="left:7px;top:299px;width:127px;height:24px;background:#fff;padding:5px 9px">Type message here</div>
</section>

<div class="abs chart-bar">
  <div class="abs" style="left:15px;top:10px;width:110px;height:30px;background:#fff"></div>
  <div class="ctrl" style="left:125px;width:35px">1D</div><div class="caret" style="left:158px"></div>
  <div class="ctrl" style="left:191px;width:98px">Chart</div><div class="caret" style="left:288px"></div>
  <div class="ctrl" style="left:319px;width:97px">Studies</div><div class="caret" style="left:415px"></div>
  <div class="ctrl" style="left:445px;width:25px"></div><div class="caret" style="left:470px"></div>
  <div class="ctrl" style="left:500px;width:22px">F</div>
</div>
<div class="abs tool-bar">
  <div class="ctrl" style="left:10px;top:12px;width:82px;font-weight:400">Select Tool</div><div class="caret" style="left:92px;top:12px"></div>
  <div class="abs" style="left:303px;top:12px;line-height:16px">O:&nbsp; 141.93<br>C:&nbsp; 141.02</div>
  <div class="abs" style="left:379px;top:12px;line-height:16px">H:&nbsp; 142.10<br>L:&nbsp;&nbsp; 140.80</div>
  <div class="abs" style="left:454px;top:12px">V:&nbsp; 119.9m</div>
</div>
<svg class="abs" style="left:290px;top:313px" width="541" height="260" viewBox="0 0 541 260">
  <rect x="0.5" y="0.5" width="540" height="259" fill="#fff" stroke="#ccc"/>
  <g stroke="#d0d0d0"><line x1="0" y1="49" x2="540" y2="49"/><line x1="0" y1="102" x2="540" y2="102"/><line x1="0" y1="154" x2="540" y2="154"/><line x1="0" y1="207" x2="540" y2="207"/></g>
  <polygon fill="#def4fd" points="0,259 0,143 10,150 22,146 58,135 68,140 148,92 158,99 175,92 230,145 270,145 295,171 312,155 350,172 392,117 422,117 444,154 460,133 486,180 500,167 510,165 530,172 540,160 540,259"/>
  <polyline fill="none" stroke="#9fd6ee" points="0,143 10,150 22,146 58,135 68,140 148,92 158,99 175,92 230,145 270,145 295,171 312,155 350,172 392,117 422,117 444,154 460,133 486,180 500,167 510,165 530,172 540,160"/>
</svg>
<div class="dates"><span style="left:341px">05 Apr</span><span style="left:422px">10 Apr</span><span style="left:503px">15 Apr</span><span style="left:584px">20 Apr</span><span style="left:665px">25 Apr</span><span style="left:746px">30 Apr</span></div>
<div class="abs" style="left:289px;top:629px;width:542px;height:2px;background:var(--line)"></div>

<section class="abs" style="left:289px;top:654px;width:540px">
  <div class="tabs" style="height:25px"><span class="on" style="padding:5px 7px">Orders</span><span style="padding:5px 8px">History</span><span style="padding:5px 8px">Transactions</span></div>
  <div style="height:26px;margin-top:1px;padding:7px 10px;display:flex;background:var(--blue-bright);color:#fff"><span style="width:124px">Ticker</span><span style="width:260px">Time ▴</span><span style="width:79px">Price ⇕</span><span>Volume</span></div>
  <div>
    <div class="row"><span style="width:124px">BTC/USD</span><span style="width:260px">12:23 12.10.2014</span><span style="width:79px">634.34</span><span>0.23</span></div>
    <div class="row"><span style="width:124px">BTC/USD</span><span style="width:260px">12:23 12.10.2014</span><span style="width:79px">634.34</span><span>0.23</span></div>
    <div class="row"><span style="width:124px">BTC/USD</span><span style="width:260px">12:23 12.10.2014</span><span style="width:79px">634.34</span><span>0.23</span></div>
  </div>
</section>

<section class="abs" style="left:849px;top:210px;width:220px">
  <div style="display:flex;height:26px;font-size:14px;text-align:center">
    <div style="flex:1;background:var(--blue);color:#fff;padding-top:4px">MARKET</div>
    <div style="flex:1;background:var(--dark);color:#fff;padding-top:4px">LIMIT</div>
  </div>
  <div style="height:3px;background:var(--blue)"></div>
  <div style="display:flex;text-align:center">
    <div style="flex:1;background:#bfe3f3">
      <div style="height:51px;padding-top:8px;font-size:14px;line-height:17px">Limit SELL<br><span style="font-size:13px">157</span><span style="font-size:17px">5.60</span></div>
      <div style="height:23px;background:#def1fa;padding-top:5px">Qty&nbsp; 20.0</div>
    </div>
    <div style="flex:1;background:var(--grey-light)">
      <div style="height:51px;padding-top:8px;font-size:14px;line-height:17px">Limit BUY<br><span style="font-size:13px">157</span><span style="font-size:17px">5.71</span></div>
      <div style="height:23px;background:var(--grey);padding-top:5px">Qty&nbsp; 20.0</div>
    </div>
  </div>
  <div class="abs" style="left:98px;top:38px;width:2px;height:32px;background:#e08a1a"></div>
  <div class="abs" style="top:108px;left:0">Quantity</div>
  <div class="abs" style="top:108px;left:72px">Limit</div>
  <div class="abs field" style="top:125px;left:0;width:67px;color:#333;font-size:13px">50</div>
  <div class="abs field" style="top:125px;left:72px;width:148px;color:#333;font-size:13px">1576.63</div>
</section>

<section class="abs obook" style="left:849px;top:370px;width:220px">
  <div class="panel-head" style="display:flex"><span style="width:112px">PRICE</span><span>VOLUME</span></div>
  <div>
    <div class="row b1"><span>123</span><span>0.233</span></div><div class="row b2"><span>122</span><span>0.334</span></div>
    <div class="row b1"><span>123</span><span>0.233</span></div><div class="row b2"><span>122</span><span>0.334</span></div>
    <div class="row b1"><span>123</span><span>0.233</span></div><div class="row b2"><span>122</span><span>0.334</span></div>
    <div class="row b1"><span>123</span><span>0.233</span></div><div class="row b2"><span>122</span><span>0.334</span></div>
    <div class="row s1"><span>123</span><span>0.233</span></div><div class="row s2"><span>122</span><span>0.334</span></div>
    <div class="row s1"><span>123</span><span>0.233</span></div><div class="row s2"><span>122</span><span>0.334</span></div>
    <div class="row s1"><span>123</span><span>0.233</span></div><div class="row s2"><span>122</span><span>0.334</span></div>
    <div class="row s1"><span>123</span><span>0.233</span></div><div class="row s2"><span>122</span><span>0.334</span></div>
  </div>
</section>

<footer class="abs footer">
  <div class="abs brand" style="left:131px;top:52px;color:#fff">Quarnel Asset Exchange</div>
  <div class="abs" style="left:277px;top:40px;width:1px;height:70px;background:#fff"></div>
  <div class="abs" style="left:290px;top:50px;width:16px;height:16px;border-radius:50%;background:#fff"></div>
  <div class="abs" style="left:131px;top:122px;font-size:10px;line-height:13px">© 2014 Quarnel Asset Exchange.<br>All rights reserved</div>
  <div class="fcol" style="left:453px"><h3>ABOUT</h3><p>Who we are<br>Trade<br>Fees<br>News<br>Legal</p></div>
  <div class="fcol" style="left:707px"><h3>HELP</h3><p>What is a Bitcoin?<br>How to buy a bitcoin?<br>How to sell a bitcoin?<br>FAQ<br>Contact US</p></div>
  <div class="fcol" style="left:940px"><h3 style="font-size:21px">FOLLOW QAX</h3>
    <div style="margin-top:6px"><span class="social"></span><span class="social"></span><span class="social"></span><span class="social"></span></div></div>
  <div class="abs" role="img" aria-label="Handwritten tagline: Change the world one bitcoin at a time" style="left:508px;top:182px;width:572px;height:72px;background:linear-gradient(90deg,rgba(255,255,255,.08),rgba(255,255,255,.18),rgba(255,255,255,.08));border-radius:4px"></div>
</footer>
</body>
</html>
```